law firm website

We need a website for our law firm that is based in Kabul, Afghanistan. We provide legal and government affairs services for the international community. We would like to see designs that use the colors of our logo, designs that are elegant and simple, yet not boring or over the top. No law or law related symbols or pictures. We would like clocks that show times for Kabul, Dubai and Washington DC.
Reason: No designs that are up to the task as yet. Perhaps we should stop using picture of people, that obviously don't work with us, in the website. If you are to use pictures, please try using pictures of Afghanistan mountains, art, craft etc. Also, please make the clocks very small - they seem to be dominating the website. We do not sell clocks or watches - we are a law firm. Hope you all understand and thank you for your designs to date.
Deal All,
Industry/Entity Type
Government
Requirements
Must have
- our logo.
the following phrases/words in flash.
"international standards" "local expertise" "integrity" "clarity" "commitment" "Afghanistan"
clocks: kabul, dubai, washington dc
Should not have
- law related pictures
afghanistan flag colors

```html
<!DOCTYPE html>
<html lang="en">
<head>
<meta charset="utf-8">
<title>Hindukush Legal Partners</title>
<link rel="stylesheet" href="https://fonts.googleapis.com/css2?family=Open+Sans:ital,wght@0,400;0,600;0,700;1,400&family=Roboto+Condensed:wght@400;700&family=Cinzel:wght@400&display=swap">
<style>
:root{
  --blue:#35a6dc;
  --blue-dark:#1e93cc;
  --band:#0aa0d8;
  --ink:#2a2a2a;
  --text:#444;
  --muted:#777;
  --nav:#2b2b2b;
  --page:#f2f2f2;
  --white:#fff;
  --footer:#343434;
  --footer-text:#d8d8d8;
  --rule:#cfcfcf;
}
*{box-sizing:border-box;margin:0;padding:0}
html,body{width:1075px;height:1200px;overflow:hidden}
body{font-family:"Open Sans",sans-serif;background:var(--white);color:var(--text);position:relative}
.abs{position:absolute}

/* header */
.header{position:absolute;left:0;top:0;width:1075px;height:137px;background:var(--page);border-bottom:1px solid #ddd}
.brand{position:absolute;left:130px;top:30px;display:flex;align-items:center;gap:12px}
.brand-mark{width:14px;height:14px;background:var(--blue)}
.brand-name{font-size:15px;font-weight:600;color:var(--ink);line-height:1.25;letter-spacing:.5px}
.clock{position:absolute;top:9px;width:100px;text-align:center}
.clock svg{width:67px;height:67px;display:block;margin:0 auto}
.clock span{display:block;font-family:"Cinzel",serif;font-size:13px;color:var(--ink);margin-top:3px;letter-spacing:.5px}

/* nav */
.nav{position:absolute;left:126px;top:116px;width:823px;height:42px;background:var(--nav);border-radius:3px;display:flex;align-items:center;padding-left:26px}
.nav a{font-size:14px;color:#f2f2f2;text-decoration:none;margin-right:41px}
.nav a.active{color:var(--blue)}
.nav .pill{position:absolute;left:542px;top:6px;width:82px;height:30px;background:var(--white);border-radius:2px;color:var(--blue);font-weight:700;display:flex;align-items:center;justify-content:center;margin:0}
.search{position:absolute;left:640px;top:8px;width:174px;height:27px;background:#555;border-radius:2px;color:#bbb;font-size:11px;padding:6px 7px}
.search svg{position:absolute;right:6px;top:6px}

/* slider */
.slider{position:absolute;left:126px;top:175px;width:823px;height:336px;border:1px solid #d4d4d4;background:var(--white);padding:4px}
.slider-img{width:100%;height:100%;background:linear-gradient(90deg,#d9cfc7 0%,#efece8 35%,#cfd3d6 70%,#8e9498 100%)}
.caption{position:absolute;left:297px;top:72px;width:493px;height:146px;background:rgba(245,245,245,.93);padding:10px 17px}
.caption h2{font-family:"Roboto Condensed",sans-serif;font-weight:700;font-size:35px;color:var(--blue);letter-spacing:.3px;line-height:1.1}
.caption p{font-family:"Roboto Condensed",sans-serif;font-size:20px;line-height:25px;color:#333;margin-top:8px}
.dots{position:absolute;right:18px;bottom:14px;display:flex;gap:7px}
.dots i{width:11px;height:11px;border-radius:50%;background:#ddd;display:block}
.dots i.on{background:var(--blue)}

/* welcome */
.welcome{position:absolute;left:128px;top:532px;width:529px}
.welcome .pre{font-size:17px;color:var(--ink)}
.welcome h1{font-weight:400;font-size:26px;color:var(--blue);line-height:1.1;padding-bottom:8px;border-bottom:1px dashed var(--rule)}
.welcome p{font-size:11px;line-height:20px;text-align:justify;margin-top:7px}
.btn-more{position:absolute;left:126px;top:780px;width:60px;height:25px;background:#ececec;font-size:11px;font-weight:700;color:var(--ink);display:flex;align-items:center;justify-content:center;gap:4px;border-radius:2px}

/* services */
.services{position:absolute;left:697px;top:527px;width:252px;height:278px;background:var(--blue);border:2px solid #fff;box-shadow:0 0 3px #bbb}
.services .tab{position:absolute;left:44px;top:-2px;width:162px;height:43px;background:#fff;box-shadow:0 2px 3px rgba(0,0,0,.2);display:flex;align-items:center;justify-content:center;gap:6px;font-size:20px;color:var(--ink)}
.services .tab b{font-weight:700}
.services .lead{position:absolute;left:8px;top:56px;width:240px;font-size:12px;font-weight:700;color:#fff;line-height:18px}
.services ul{position:absolute;left:0;top:101px;width:100%;list-style:none}
.services li{height:34px;border-top:1px solid #5cbbe6;font-size:15px;color:#fff;padding:6px 9px;position:relative}
.services li.on{background:#3a3a3a}
.services li.on svg{position:absolute;right:10px;top:10px}
.services .more{position:absolute;right:10px;bottom:9px;font-size:11px;font-weight:700;color:#1a2a33}

/* band */
.band{position:absolute;left:0;top:822px;width:1075px;height:161px;background:#f3f3f3;border-top:1px solid #ddd}
.sec-title{position:absolute;display:flex;align-items:center;gap:9px;font-size:18px;color:var(--ink);padding-bottom:9px;border-bottom:1px dashed var(--rule)}
.sec-title em{font-style:normal;color:var(--blue)}
.quote{position:absolute;top:890px;width:255px;display:flex;gap:8px}
.avatar{width:64px;height:67px;border:1px solid #ccc;background:#fff;padding:3px;flex:none}
.avatar div{width:100%;height:100%;background:linear-gradient(180deg,#e8e8e8,#b9b4ae)}
.quote p{font-size:11px;line-height:16px;color:#333}
.quote p b{font-weight:700}
.quote .by{display:block;margin-top:5px;color:var(--blue);font-weight:600}
.arrows{position:absolute;left:913px;top:845px;display:flex;gap:5px}
.arrows i{width:15px;height:15px;border-radius:50%;border:1px solid #bbb;background:#fff;display:block}
.ethic{position:absolute;left:696px;top:888px;width:252px;display:flex;gap:8px;font-size:11px;font-weight:700;color:#333;line-height:15px}
.ethic-more{position:absolute;left:906px;top:938px;font-size:11px;font-weight:700;color:#222}

/* newsletter */
.news{position:absolute;left:0;top:983px;width:1075px;height:43px;background:var(--band)}
.news h3{position:absolute;left:128px;top:11px;font-size:16px;font-weight:700;color:#fff}
.news .field{position:absolute;left:444px;top:7px;width:193px;height:28px;background:#fff;font-size:10px;font-style:italic;color:#999;padding:6px 7px}
.news .sub{position:absolute;left:644px;top:7px;width:88px;height:28px;background:#1a1a1a;color:#fff;font-size:12px;font-weight:700;display:flex;align-items:center;justify-content:center}
.social{position:absolute;left:846px;top:9px;display:flex;gap:3px}
.social i{width:24px;height:24px;border-radius:50%;background:#fff;border:2px solid #dff2fb;display:block}

/* footer */
.footer{position:absolute;left:0;top:1026px;width:1075px;height:174px;background:var(--footer);color:var(--footer-text)}
.footer h4{position:absolute;font-weight:400;font-size:17px;color:#f0f0f0;padding-bottom:7px;border-bottom:1px solid #777}
.links{position:absolute;top:53px;list-style:none;font-size:11px;line-height:21px}
.links li::before{content:"›";margin-right:5px;color:#aaa}
.office{position:absolute;top:56px;width:210px;font-size:11px;line-height:17px}
.office b{display:block;font-size:12px;color:#fff;margin-bottom:4px}
.row{display:flex;gap:10px;margin-bottom:5px;align-items:flex-start}
.row svg{flex:none;margin-top:2px}
.vr{position:absolute;top:10px;width:1px;height:154px;background:#2a2a2a;border-right:1px solid #444}
.foot-brand{position:absolute;left:760px;top:80px;width:190px;text-align:center;font-size:11px;line-height:17px}
.foot-brand .name{font-size:14px;font-weight:600;color:#888;margin-bottom:14px}
</style>
</head>
<body>

<header class="header">
  <div class="brand"><span class="brand-mark"></span><span class="brand-name">Hindukush<br>Legal Partners</span></div>

  <div class="clock" style="left:592px">
    <svg viewBox="0 0 70 70"><circle cx="35" cy="35" r="32" fill="#fff" stroke="#35a6dc" stroke-width="4"/><g stroke="#333" stroke-width="1.2"><line x1="35" y1="7" x2="35" y2="11"/><line x1="63" y1="35" x2="59" y2="35"/><line x1="35" y1="63" x2="35" y2="59"/><line x1="7" y1="35" x2="11" y2="35"/></g><line x1="35" y1="35" x2="35" y2="14" stroke="#222" stroke-width="1.6"/><line x1="35" y1="35" x2="22" y2="40" stroke="#222" stroke-width="2"/></svg>
    <span>Kabul</span>
  </div>
  <div class="clock" style="left:710px">
    <svg viewBox="0 0 70 70"><circle cx="35" cy="35" r="32" fill="#fff" stroke="#35a6dc" stroke-width="4"/><g stroke="#333" stroke-width="1.2"><line x1="35" y1="7" x2="35" y2="11"/><line x1="63" y1="35" x2="59" y2="35"/><line x1="35" y1="63" x2="35" y2="59"/><line x1="7" y1="35" x2="11" y2="35"/></g><line x1="35" y1="35" x2="26" y2="18" stroke="#222" stroke-width="1.6"/><line x1="35" y1="35" x2="48" y2="44" stroke="#222" stroke-width="2"/></svg>
    <span>Dubai</span>
  </div>
  <div class="clock" style="left:836px">
    <svg viewBox="0 0 70 70"><circle cx="35" cy="35" r="32" fill="#fff" stroke="#35a6dc" stroke-width="4"/><g stroke="#333" stroke-width="1.2"><line x1="35" y1="7" x2="35" y2="11"/><line x1="63" y1="35" x2="59" y2="35"/><line x1="35" y1="63" x2="35" y2="59"/><line x1="7" y1="35" x2="11" y2="35"/></g><line x1="35" y1="35" x2="50" y2="22" stroke="#222" stroke-width="1.6"/><line x1="35" y1="35" x2="24" y2="46" stroke="#222" stroke-width="2"/></svg>
    <span>Washington DC</span>
  </div>
</header>

<nav class="nav">
  <a class="active">About</a><a>People</a><a>Services</a><a>Ethics</a><a>Publications</a><a>Contact</a>
  <a class="pill">LexOrbit</a>
  <div class="search">Search
    <svg width="14" height="14" viewBox="0 0 14 14"><circle cx="6" cy="6" r="4.5" fill="none" stroke="#111" stroke-width="1.8"/><line x1="9.2" y1="9.2" x2="13" y2="13" stroke="#111" stroke-width="2"/></svg>
  </div>
</nav>

<section class="slider">
  <div class="slider-img" role="img" aria-label="Photograph of a professional in a bright office with bookshelves"></div>
  <div class="caption">
    <h2>INTERNATIONAL STANDARDS</h2>
    <p>Lorem ipsum dolor sit amet, consectetue adipiscing elit, sed diam nonummy nibh euismod tincidunt ut laoreet dolore magna aliquam erat volutpat.</p>
  </div>
  <div class="dots"><i class="on"></i><i></i><i></i><i></i></div>
</section>

<section class="welcome">
  <div class="pre">Welcome to</div>
  <h1>Hindukush Legal Partners</h1>
  <p>Hindukush Legal Partners (HLP) is an Afghan legal and government affairs advisory firm staffed by a number of highly experienced lawyers and advisors qualified in Afghanistan, the United States and Australia.</p>
  <p>The two principals of HLP have over a decade of legal and government affairs advisory experience in Afghanistan advising investors, local and foreign government agencies and non-governmental organisations on some of the largest and most complex matters, transactions, projects and financings across several sectors including mining and infrastructure, telecommunications, oil &amp; gas, construction, media, aviation and banking and financial services.</p>
</section>
<div class="btn-more">More <svg width="9" height="8" viewBox="0 0 9 8"><path d="M1 1l3 3-3 3M5 1l3 3-3 3" fill="none" stroke="#222" stroke-width="1.2"/></svg></div>

<aside class="services">
  <div class="tab"><b>HLP</b> SERVICES</div>
  <p class="lead">We provide exceptional, practical and cost-effective services</p>
  <ul>
    <li>Corporate and investment</li>
    <li class="on">Projects <svg width="14" height="12" viewBox="0 0 14 12"><path d="M1 1l5 5-5 5M7 1l5 5-5 5" fill="none" stroke="#bbb" stroke-width="1.5"/></svg></li>
    <li>Commercial contracts</li>
    <li>Financings</li>
  </ul>
  <div class="more">More »</div>
</aside>

<section class="band"></section>
<div class="sec-title" style="left:128px;top:842px;width:529px">
  <svg width="18" height="16" viewBox="0 0 18 16"><rect x="0" y="0" width="11" height="8" rx="2" fill="#35a6dc"/><rect x="6" y="5" width="11" height="8" rx="2" fill="#1e93cc"/><path d="M13 13l2 3v-3z" fill="#1e93cc"/></svg>
  <span>Our <em>Client Says</em></span>
</div>
<div class="quote" style="left:126px">
  <div class="avatar"><div role="img" aria-label="Portrait photo of a client"></div></div>
  <p><b>“ Lorem ipsum dolor sit amet,</b> sed diam nonummy nibh euismod tincidunt ut laor dolore magna <span class="by">- Lorem ipsum dolor</span></p>
</div>
<div class="quote" style="left:407px">
  <div class="avatar"><div role="img" aria-label="Portrait photo of a client"></div></div>
  <p><b>“ Lorem ipsum dolor sit amet,</b> sed diam nonummy nibh euismod tincidunt ut laor dolore magna <span class="by">- Lorem ipsum dolor</span></p>
</div>

<div class="sec-title" style="left:696px;top:842px;width:252px">
  <svg width="15" height="16" viewBox="0 0 15 16"><rect x="1" y="1" width="12" height="14" fill="none" stroke="#35a6dc" stroke-width="1.6"/><path d="M4 10l3-3 2 2 3-4" fill="none" stroke="#35a6dc" stroke-width="1.4"/></svg>
  <span>Ethics</span>
</div>
<div class="arrows"><i></i><i></i></div>
<div class="ethic">
  <svg width="13" height="13" viewBox="0 0 13 13" style="flex:none"><circle cx="6.5" cy="6.5" r="5.5" fill="none" stroke="#35a6dc" stroke-width="1.2"/><path d="M3.5 6.5l2 2 4-4" fill="none" stroke="#35a6dc" stroke-width="1.6"/></svg>
  <span>Maintain the highest standards of integrity, fairness, honesty and respect in all our dealings.</span>
</div>
<div class="ethic-more">More »</div>

<section class="news">
  <h3>Keep up to date with our latest news.</h3>
  <div class="field">Enter your email here</div>
  <div class="sub">SUBSCRIBE</div>
  <div class="social"><i></i><i></i><i></i><i></i></div>
</section>

<footer class="footer">
  <h4 style="left:127px;top:17px;width:170px">Quick Links</h4>
  <ul class="links" style="left:127px"><li>Home</li><li>People</li><li>Services</li><li>Ethics</li></ul>
  <ul class="links" style="left:203px"><li>Publications</li><li>Testimonials</li><li>Contact</li></ul>
  <div class="vr" style="left:308px"></div>
  <h4 style="left:320px;top:17px;width:411px">Contact Information</h4>
  <div class="office" style="left:323px">
    <b>Kabul Office</b>
    <div class="row"><svg width="12" height="15" viewBox="0 0 12 15"><path d="M6 0a5 5 0 0 1 5 5c0 4-5 10-5 10S1 9 1 5a5 5 0 0 1 5-5z" fill="#35a6dc"/><circle cx="6" cy="5" r="1.8" fill="#343434"/></svg><span>Floor 3 Cedar Court, Block C, Wazir Akbar Khan, Kabul, Afghanistan</span></div>
    <div class="row"><svg width="12" height="12" viewBox="0 0 12 12"><path d="M2 0l3 3-1.5 1.5a7 7 0 0 0 4 4L9 7l3 3-2 2C5 12 0 7 0 2z" fill="#35a6dc"/></svg><span>93-700-214-385</span></div>
    <div class="row"><svg width="13" height="10" viewBox="0 0 13 10"><rect width="13" height="10" fill="#35a6dc"/><path d="M0 0l6.5 5L13 0" fill="none" stroke="#343434" stroke-width="1"/></svg><span>office@hlpartners.af</span></div>
  </div>
  <div class="office" style="left:528px">
    <b>Dubai Office</b>
    <div class="row"><svg width="12" height="15" viewBox="0 0 12 15"><path d="M6 0a5 5 0 0 1 5 5c0 4-5 10-5 10S1 9 1 5a5 5 0 0 1 5-5z" fill="#35a6dc"/><circle cx="6" cy="5" r="1.8" fill="#343434"/></svg><span>Suite 902 Harbor Point Tower, Marina Walk, Dubai, UAE</span></div>
    <div class="row"><svg width="12" height="12" viewBox="0 0 12 12"><path d="M2 0l3 3-1.5 1.5a7 7 0 0 0 4 4L9 7l3 3-2 2C5 12 0 7 0 2z" fill="#35a6dc"/></svg><span>971 502 118 736</span></div>
    <div class="row"><svg width="13" height="10" viewBox="0 0 13 10"><rect width="13" height="10" fill="#35a6dc"/><path d="M0 0l6.5 5L13 0" fill="none" stroke="#343434" stroke-width="1"/></svg><span>office@hlpartners.af</span></div>
  </div>
  <div class="vr" style="left:745px"></div>
  <div class="foot-brand">
    <div class="name">Hindukush Legal Partners</div>
    © Hindukush Legal Partners.<br>All Rights Reserved.
  </div>
</footer>

</body>
</html>
```